Brindle Chill Supplies Stationery Design

Stationery Design

Thank you to all those who have submitted the logos. We have selected the logo for our new identity and we are now looking for stationery ideas.

The attached logo must be used in all stationery designs.

We require the following items of stationery:

1. Business Cards for 10 employees – Double Sided – All the card will have the same address:

7 – 31 Marrowby Lane, Kingston Upon Thames, Surrey, KT4 9QX, United Kingdom

Office phone number: +44 (0)208 613 7742

Freephone: 0800 129 4837

Fax: +44 (0)20 8731 2964

Website: www.brindlechill.example

The names on the cards and mobile numbers – will be given on selection of final design.

A few of the cards will have different emails but 5/6 card will have the same email address.

2. Letterhead A4 – same contact details as above – email address to be used info@brindlechill.example

3. Compliments Slip – same details as no.2

4. Envelope designs – with just the address, Freephone and Website.

Sizes Required: C4 – 324mm x 229mm – Windows and Regular

DL – 110mm x 220mm – Windows and Regular

5. A4 Ring Binder – Logo at the front and back and side; company name on the front and side of the binder (Brindle Chill Supplies); contact details at the back; same as number 2 above.

The ring binder will have food, drink and hygiene inserts inside and will act as a temporary brochure.

It may help with the design process to know we sell a range of frozen food products including chips, burgers, fish, frozen poultry items, vegetables, ice cream, desserts, bakery products, pies, pasties, onion rings, pizza toppings etc.

We also sell ambient products such as sauces, crisps such as dunmores, chocolates such as Hollensby, Vorelle, Quib etc.

Drinks wise we sell branded products such as zesta tonic, fizmo, lumra, glint, sky hare etc; As well as juices and mineral water.

We also sell hygiene products such as tissue paper, hand towels, and other washroom products, bleaches etc.

Our website doesn’t have the full range of products but gives you a good idea of what we do www.brindlechill.example

Please note we are looking for a classy, slick design so don’t worry about trying to add all the products on the binder design; these have just been given to assist with the design process.

We may add a slogan to the stationery but the final decision on this still has to be taken and the profile will be updated within the next 72 hours.

This project will only last a maximum of 10-14 days, we don’t want to drag it out like the logo so please only submit creative ideas; which have been given thought in terms of design, text and graphics.

Any questions, feel free to ask.

Thank you and we look forward to your designs.

Regards

Torvin Ashcombe

I've uploaded an Adobe Illustrator CS2.ai file, and an EPS file of my new logo so you can get better clarity within your designs for this project

Thanks
Torvin

Hi

We have had various questions in respect of dimensions and budget; we have addressed both issues below by providing dimensions and we will be increasing the budget to $500 as soon as Pixel Bazaar let us know how we can increase; they have already been emailed.

In respect of the dimensions, we have had various answers but here are the most common sizes.

 

There are various sizes of lever arch A4 folders but the most common ones are below:

 

 

• Dimensions width 28.5cm, height 32cm,spine 9cm
• Dimensions (mm)H:315 x W:285
• Dimensions (mm) H:31cm x W:27cm

 

The most common thickness in the UK seems to be 70mm; so can we use this as a guide please.

 

 

Compliment Slip Sizes:

 

• Our Compliment Slips are DL in size. You should design your Compliment Slip to DL dimension but also add a 3mm bleed around each edge.

 

Trim Size – 99mm x 210mm

 

With Bleed – 105mm – 216mm

 

 

Business Cards:

 

Trim Size: 85mm x 55mm

 

With Bleed: 91mm x 61mm

 

 

We have extended the time frame and the budget on this so look forward to new designs.

 

I hope this helps and all the best for Christmas and 2010..

 

Regards

Torvin Ashcombe.

Hi Guys

Another important point to mention as each country has different rules...

In the Uk the postage stamps go in the top right hand corner of the envelope so we will have to have our logo company details etc in either the top left or the bottom of the envelope.

Also all envelopes must have at the back our return address:

Return Address:

Brindle Chill Supplies Ltd
7 - 31 Marrowby Lane
Kingston Upon Thames
Surrey
KT4 9QX

So we could even have the business logo, name and website address at the front and the address at the back.

Regards

Torvin

```html
<!DOCTYPE html>
<html lang="en">
<head>
<meta charset="utf-8">
<title>Brindle Chill Supplies – Business Card Options</title>
<link rel="stylesheet" href="https://fonts.googleapis.com/css2?family=Didact+Gothic&family=Questrial&display=swap">
<style>
  :root {
    --backdrop: #5b3822;
    --card: #ffffff;
    --brand-blue: #1d3b8f;
    --brand-red: #c3141f;
    --sky: #8fcbeb;
    --ink: #222222;
    --muted: #8a8a8a;
    --heading: #f2ece6;
  }
  * { box-sizing: border-box; margin: 0; padding: 0; }
  html, body { width: 1200px; height: 960px; overflow: hidden; }
  body {
    background: var(--backdrop);
    font-family: "Didact Gothic", "Questrial", sans-serif;
    color: var(--ink);
    position: relative;
  }
  .column-title {
    position: absolute;
    top: 40px;
    font-family: "Questrial", sans-serif;
    font-size: 27px;
    font-weight: normal;
    letter-spacing: 6px;
    color: var(--heading);
  }
  .column-title.side-one { left: 120px; }
  .column-title.side-two { left: 700px; }

  .card {
    position: absolute;
    background: var(--card);
    overflow: hidden;
    box-shadow: 0 6px 14px rgba(0,0,0,0.35);
  }
  .card.front { left: 53px; width: 514px; height: 312px; }
  .card.back  { left: 602px; width: 526px; height: 312px; }
  .row-one { top: 144px; }
  .row-two { top: 514px; }

  .wordmark {
    position: absolute;
    display: flex;
    align-items: center;
    gap: 10px;
    color: var(--ink);
    font-family: "Didact Gothic", sans-serif;
    white-space: nowrap;
  }
  .wordmark .dot {
    border-radius: 50%;
    background: var(--brand-red);
    flex: none;
  }

  /* Soft brand-colour glow that fades to white well inside its area */
  .swirl-area {
    position: absolute;
    inset: 0;
    pointer-events: none;
  }
  .front.option-a .swirl-area {
    background: radial-gradient(circle 165px at 130px 80px,
      rgba(29,59,143,0.95) 0%,
      rgba(120,40,90,0.9) 25%,
      rgba(195,20,31,0.85) 48%,
      rgba(195,20,31,0.45) 66%,
      rgba(143,203,235,0.45) 80%,
      rgba(255,255,255,0) 100%);
  }
  .front.option-b .swirl-area {
    background: radial-gradient(circle 175px at 10px 165px,
      rgba(29,59,143,0.95) 0%,
      rgba(120,40,90,0.9) 25%,
      rgba(195,20,31,0.85) 48%,
      rgba(195,20,31,0.45) 66%,
      rgba(143,203,235,0.45) 80%,
      rgba(255,255,255,0) 100%);
  }
  .front.option-a .wordmark { right: 30px; bottom: 40px; font-size: 17px; }
  .front.option-a .wordmark .dot { width: 14px; height: 14px; }
  .front.option-b .wordmark { left: 240px; top: 138px; font-size: 23px; }
  .front.option-b .wordmark .dot { width: 18px; height: 18px; }

  .back .wordmark { top: 34px; font-size: 22px; }
  .back .wordmark .dot { width: 30px; height: 30px; }
  .back.option-a .wordmark { left: 28px; }
  .back.option-b .wordmark { right: 28px; top: 52px; }

  .person { position: absolute; top: 54px; }
  .back.option-a .person { right: 44px; text-align: left; }
  .back.option-b .person { left: 40px; top: 70px; }
  .person-name {
    font-size: 19px;
    letter-spacing: 1.5px;
    font-variant: small-caps;
    font-weight: bold;
  }
  .back.option-a .person-name { color: var(--brand-blue); }
  .back.option-b .person-name { color: var(--brand-red); }
  .person-role { font-size: 17px; font-style: italic; color: var(--muted); }

  .contact-band {
    position: absolute;
    left: 0; right: 0; top: 132px; height: 86px;
    color: #ffffff;
    font-size: 15px;
    line-height: 20px;
  }
  .band-red {
    position: absolute; inset: 0;
    background: linear-gradient(180deg, #d21a25, #a90f18);
  }
  .band-blue {
    position: absolute; top: 0; bottom: 0; left: 0; width: 58%;
    background: linear-gradient(180deg, #2b4aa6, #162f76);
    clip-path: polygon(0 0, 100% 0, 82% 100%, 0 100%);
  }
  .band-stripe {
    position: absolute; top: 0; bottom: 0; left: 0; width: 60%;
    background: #ffffff;
    clip-path: polygon(96.5% 0, 100% 0, 82% 100%, 79% 100%);
  }
  .phone-list, .address {
    position: absolute; top: 14px; list-style: none;
  }
  .phone-list { left: 30px; }
  .phone-list b { display: inline-block; width: 22px; font-weight: normal; }
  .address { right: 30px; text-align: right; }

  .web-details {
    position: absolute;
    left: 0; right: 0; top: 240px;
    text-align: center;
    font-size: 16px;
    line-height: 20px;
  }
  .back.option-a .web-details { color: var(--brand-blue); }
  .back.option-b .web-details { color: var(--brand-red); }
  .freephone { letter-spacing: 2px; }
</style>
</head>
<body>
  <h2 class="column-title side-one">SIDE 1 OPTIONS</h2>
  <h2 class="column-title side-two">SIDE 2 OPTIONS</h2>

  <section class="card front option-a row-one">
    <div class="swirl-area" role="img" aria-label="Brand symbol decoration in blue, red and light blue"></div>
    <div class="wordmark"><span class="dot"></span>Brindle Chill Supplies</div>
  </section>

  <section class="card front option-b row-two">
    <div class="swirl-area" role="img" aria-label="Brand symbol decoration in blue, red and light blue"></div>
    <div class="wordmark"><span class="dot"></span>Brindle Chill Supplies</div>
  </section>

  <section class="card back option-a row-one">
    <div class="wordmark"><span class="dot"></span>Brindle Chill Supplies</div>
    <div class="person">
      <p class="person-name">John Doe</p>
      <p class="person-role">Designation</p>
    </div>
    <div class="contact-band">
      <div class="band-red"></div>
      <div class="band-stripe"></div>
      <div class="band-blue"></div>
      <ul class="phone-list">
        <li><b>t:</b>+44 (0)208 613 7742</li>
        <li><b>f:</b>+44 (0)20 8731 2964</li>
        <li><b>m:</b>number goes in here</li>
      </ul>
      <ul class="address">
        <li>7 – 31 Marrowby Lane</li>
        <li>Kingston Upon Thames, Surrey</li>
        <li>KT4 9QX, United Kingdom</li>
      </ul>
    </div>
    <div class="web-details">
      <p>www.brindlechill.example</p>
      <p class="freephone">0800 129 4837</p>
    </div>
  </section>

  <section class="card back option-b row-two">
    <div class="wordmark"><span class="dot"></span>Brindle Chill Supplies</div>
    <div class="person">
      <p class="person-name">John Doe</p>
      <p class="person-role">Designation</p>
    </div>
    <div class="contact-band">
      <div class="band-red"></div>
      <ul class="phone-list">
        <li><b>t:</b>+44 (0)208 613 7742</li>
        <li><b>f:</b>+44 (0)20 8731 2964</li>
        <li><b>m:</b>number goes in here</li>
      </ul>
      <ul class="address">
        <li>7 – 31 Marrowby Lane</li>
        <li>Kingston Upon Thames, Surrey</li>
        <li>KT4 9QX, United Kingdom</li>
      </ul>
    </div>
    <div class="web-details">
      <p>www.brindlechill.example</p>
      <p class="freephone">0800 129 4837</p>
    </div>
  </section>
</body>
</html>
```